Kestrel Electrics - Electrician company flyers for new clients

I want a flyer that will be dropped into mailboxes and will hopefully stand out more that the ones i have tried to mock up. I have attached my latest design to give you an idea but it is rather boring.

The aim is obviously to entice new customers into calling me for any electrical work, mainly domestic but i also do commercial work.
I will also upload a photo of my business card so that it can be used as a reference and my website is www.kestrelelectrics-example.co.nz for any extra information.

Ideally the flyer will be DL size
measurements from printmondo is that's any help
Document Trim Size
99 x 210 mm
1169 x 2480 pixels
Full Bleed Size
102 x 213 mm
1205 x 2516 pixels

Target Market(s)

Domestic electrical works

Industry/Entity Type

Electrician

Requirements
Must have
• all of my contact details -
• Dean Harwood
• Dean@kestrelelectrics-example.co.nz
• 027 5832 094
• www.kestrelelectrics-example.co.nz
• A little write up similar to the one written on my draft but there's probably alot of room for improvement as my writing skills are lacking.
Nice to have
• clear and concise writing so that people wont throw it away before reading

```html
<!DOCTYPE html>
<html lang="en">
<head>
<meta charset="utf-8">
<title>Kestrel Electrics – DL Flyer</title>
<link href="https://fonts.googleapis.com/css2?family=Anton&family=Lato:wght@400;700&family=Montserrat:wght@800&display=swap" rel="stylesheet">
<style>
  :root {
    --backdrop: #202020;
    --paper: #ffffff;
    --brand-blue: #1da1dc;
    --panel-grey: #58585a;
    --ink: #111111;
    --blueprint-light: #f3f3f3;
    --blueprint-mid: #dcdcdc;
    --photo-blue: #2d5fb4;
    --photo-warm: #d9c4ae;
  }
  * { margin: 0; padding: 0; box-sizing: border-box; }
  html, body { width: 1200px; height: 1200px; overflow: hidden; background: var(--backdrop); }
  .flyer {
    position: absolute; left: 366px; top: 74px;
    width: 635px; height: 1346px;
    background: var(--paper);
    transform: scale(0.8); transform-origin: top left;
    overflow: hidden;
    font-family: "Lato", sans-serif;
  }
  .hero-image {
    position: absolute; left: 0; top: 98px; width: 635px; height: 578px;
    background: linear-gradient(100deg, var(--blueprint-mid) 0%, var(--blueprint-light) 45%, #e4e4e4 75%, #f7f7f7 100%);
  }
  .headline-box {
    position: absolute; left: 236px; top: 34px; width: 353px; height: 549px;
    background: var(--brand-blue); color: var(--paper);
    padding: 16px 18px 0 18px;
  }
  .headline {
    font-family: "Anton", sans-serif; font-weight: 400;
    font-size: 66px; line-height: 67px; letter-spacing: -0.5px;
    text-transform: uppercase;
  }
  .headline .last { font-size: 56px; line-height: 60px; display: block; }
  .headline-rule { width: 288px; height: 8px; background: var(--paper); margin: 6px 0 14px 0; }
  .intro { font-size: 22px; line-height: 27px; }
  .what-we-do {
    position: absolute; left: 88px; top: 720px; width: 181px; height: 305px;
    border: 6px solid var(--brand-blue);
    font-family: "Montserrat", sans-serif; font-weight: 800;
    font-size: 46px; line-height: 54px; color: var(--ink);
    text-align: right; padding: 40px 6px 0 0;
    z-index: 2;
  }
  .what-we-do span { display: block; }
  .work-photo {
    position: absolute; left: 0; top: 1008px; width: 317px; height: 338px;
    background: linear-gradient(120deg, var(--photo-blue) 0%, #4a78c8 35%, var(--photo-warm) 70%, #efe6dc 100%);
  }
  .contact-panel {
    position: absolute; left: 317px; top: 676px; width: 318px; height: 405px;
    background: var(--panel-grey); color: var(--paper);
  }
  .panel-notch { position: absolute; left: 0; top: 162px; }
  .about { position: absolute; left: 32px; top: 18px; width: 270px; font-size: 22px; line-height: 27px; }
  .contact { position: absolute; left: 0; top: 212px; width: 318px; text-align: center; font-weight: 700; }
  .contact-title { font-size: 31px; line-height: 40px; }
  .contact-name { font-size: 30px; line-height: 40px; margin-top: 6px; }
  .contact-phone { font-size: 27px; line-height: 32px; display: flex; align-items: center; justify-content: center; gap: 6px; }
  .contact-lines { position: absolute; left: 6px; top: 340px; font-size: 16.5px; line-height: 27px; font-weight: 400; }
  .contact-lines div { display: flex; align-items: center; gap: 5px; white-space: nowrap; }
  .brand-name {
    position: absolute; left: 317px; top: 1081px; width: 318px; height: 265px;
    display: flex; align-items: center; justify-content: center; gap: 10px;
    font-size: 34px; font-weight: 700; color: var(--brand-blue); line-height: 36px;
  }
  .brand-square { width: 26px; height: 26px; background: var(--brand-blue); }
</style>
</head>
<body>
<main class="flyer">
  <div class="hero-image" role="img" aria-label="Architectural floor plan blueprints with rolled plans"></div>

  <section class="headline-box">
    <h1 class="headline">Do you need<br>a local &amp;<br>reliable<span class="last">electrician?</span></h1>
    <div class="headline-rule"></div>
    <p class="intro">Specializing in residential and commercial electrical services, we are dedicated to providing customer service that is second to none. Whether you need a small wiring fix or the full installation, we can get the job done right.</p>
  </section>

  <h2 class="what-we-do"><span>WHAT</span><span>WE</span><span>DO</span></h2>

  <div class="work-photo" role="img" aria-label="Electrician in blue cap and shirt installing a light fitting"></div>

  <section class="contact-panel">
    <svg class="panel-notch" width="32" height="70" viewBox="0 0 32 70"><polygon points="0,0 32,35 0,70" fill="#ffffff"/></svg>
    <p class="about">Based in Harbourview, We are your local Electricians with our main aim to keep our work and communication to a very high standard.</p>
    <div class="contact">
      <div class="contact-title">Contact Us Today !</div>
      <div class="contact-name">Dean Harwood</div>
      <div class="contact-phone">
        <svg width="24" height="24" viewBox="0 0 24 24" fill="none" stroke="#fff" stroke-width="1.6"><circle cx="12" cy="12" r="10.5"/><path d="M8.5 7.5c-.8.8-.6 2.6 1.2 4.8s3.9 3 4.8 2.2l.9-.9-1.8-1.6-.9.7c-.6-.2-1.8-1.4-2.1-2.1l.7-.9-1.6-1.8z" fill="#fff"/></svg>
        027 5832 094
      </div>
    </div>
    <div class="contact-lines">
      <div><svg width="18" height="13" viewBox="0 0 18 13" fill="none" stroke="#fff" stroke-width="1.4"><rect x="1" y="1" width="16" height="11"/><path d="M1 1l8 6 8-6M1 12l6-5M17 12l-6-5"/></svg>Dean@kestrelelectrics-example.co.nz</div>
      <div><svg width="17" height="17" viewBox="0 0 17 17" fill="none" stroke="#fff" stroke-width="1.2"><circle cx="8.5" cy="8.5" r="7.5"/><ellipse cx="8.5" cy="8.5" rx="3.2" ry="7.5"/><path d="M1 8.5h15M2.2 4.8h12.6M2.2 12.2h12.6"/></svg>www.kestrelelectrics-example.co.nz</div>
    </div>
  </section>

  <div class="brand-name"><span class="brand-square"></span><span>Kestrel<br>Electrics</span></div>
</main>
</body>
</html>
```